Business Card - Professional Minimalist - Double sided

We appreciate minimalist logo/web/collateral designs that allow design to tell a story. We want to relay a professional image/approach but throwing in a splash of modern when we’re able so long as it’s not distracting. Think 75% classic corporate, 25% modern. Open to black or white design, not sure which might look the best.

Target Market(s)

Senior executives or related government affairs contacts within the agriculture, energy, and defense industries (i.e., potential clients) but located outside of Washington, DC. Most potential clients based in DC with be familiar with both of us and our shared history.

Industry/Entity Type

Consulting

Contact Information for Business Card

Name: Daniel R. Whitlock
Title: Co-Founder & Partner
Address: 418 Bramblewood Ave. SE | Suite 2716 | Washington, D.C. 20019
Phone: (202) 555-0187
Email: Daniel@HollerbyWhitlock.com

Font styles to use
Serif

Colors

Designer to choose only greyscale colors for use in the design.

Requirements
Must have
• Name: Daniel R. Whitlock
Phone: (202) 555-0187

```html
<!DOCTYPE html>
<html lang="en">
<head>
<meta charset="utf-8">
<title>Hollerby Whitlock Group – Business Card</title>
<link href="https://fonts.googleapis.com/css2?family=Montserrat:wght@400;500&display=swap" rel="stylesheet">
<style>
  :root {
    --page: #ffffff;
    --card: #000000;
    --ink: #c4c4c4;
    --ink-soft: #b0b0b0;
    --icon: #8a8a8a;
    --band-light: #3a3a3a;
    --band-dark: #1c1c1c;
  }
  * { margin: 0; padding: 0; box-sizing: border-box; }
  html, body {
    width: 1200px;
    height: 846px;
    overflow: hidden;
    background: var(--page);
    font-family: "Montserrat", sans-serif;
  }
  .card {
    position: absolute;
    left: 270px;
    width: 660px;
    height: 377px;
    background: var(--card);
    overflow: hidden;
  }
  .card--front { top: 45px; }
  .card--back { top: 435px; left: 269px; }

  .pattern-band {
    position: absolute;
    left: 0;
    top: 0;
    width: 660px;
    height: 377px;
  }

  .brand {
    position: absolute;
    left: 225px;
    top: 168px;
    display: flex;
    align-items: center;
    gap: 14px;
  }
  .brand__mark {
    width: 44px;
    height: 44px;
    border: 3px solid var(--ink-soft);
  }
  .brand__name {
    color: var(--ink-soft);
    font-weight: 500;
    font-size: 25px;
    letter-spacing: 1.5px;
    text-transform: uppercase;
    line-height: 1.05;
  }
  .brand__name span { display: block; font-size: 15px; letter-spacing: 7px; text-align: right; }

  .person {
    position: absolute;
    left: 60px;
    top: 99px;
    color: var(--ink);
  }
  .person__name { font-size: 22px; font-weight: 400; line-height: 1.1; }
  .person__title { font-size: 13px; font-weight: 400; margin-top: 1px; }

  .contact {
    position: absolute;
    left: 281px;
    top: 98px;
    list-style: none;
    color: var(--ink);
    font-size: 15px;
    line-height: 19px;
  }
  .contact__item {
    display: flex;
    align-items: flex-start;
    margin-bottom: 13px;
  }
  .contact__icon {
    width: 22px;
    height: 22px;
    margin-right: 19px;
    flex: none;
    fill: none;
    stroke: var(--icon);
    stroke-width: 1.6;
  }
  .contact__icon--solid { fill: var(--icon); stroke: none; }
</style>
</head>
<body>

<section class="card card--front">
  <svg class="pattern-band" viewBox="0 0 660 377" role="img" aria-label="Decorative outlined leaf pattern band across the top corner">
    <defs>
      <linearGradient id="bandFront" x1="0" y1="0" x2="1" y2="0">
        <stop offset="0" stop-color="var(--band-light)"/>
        <stop offset="1" stop-color="var(--band-dark)"/>
      </linearGradient>
    </defs>
    <polygon points="0,0 654,0 0,131" fill="url(#bandFront)"/>
  </svg>

  <div class="brand">
    <div class="brand__mark"></div>
    <div class="brand__name">Hollerby Whitlock<span>Group</span></div>
  </div>
</section>

<section class="card card--back">
  <svg class="pattern-band" viewBox="0 0 660 377" role="img" aria-label="Decorative outlined leaf pattern band across the bottom corner">
    <defs>
      <linearGradient id="bandBack" x1="0" y1="0" x2="1" y2="0">
        <stop offset="0" stop-color="var(--band-dark)"/>
        <stop offset="1" stop-color="var(--band-light)"/>
      </linearGradient>
    </defs>
    <polygon points="21,377 660,247 660,377" fill="url(#bandBack)"/>
  </svg>

  <div class="person">
    <h1 class="person__name">Daniel R. Whitlock</h1>
    <p class="person__title">Co-Founder &amp; Partner</p>
  </div>

  <ul class="contact">
    <li class="contact__item">
      <svg class="contact__icon" viewBox="0 0 22 22">
        <path d="M11 20c-4-5-6-8-6-11a6 6 0 0 1 12 0c0 3-2 6-6 11z"/>
        <circle cx="11" cy="9" r="2.2"/>
      </svg>
      <span>418 Bramblewood Ave. SE<br>Suite 2716 | Washington, D.C. 20019</span>
    </li>
    <li class="contact__item">
      <svg class="contact__icon contact__icon--solid" viewBox="0 0 22 22">
        <path d="M5 2l4 4-2 3c1 2 3 4 5 5l3-2 4 4-3 3C10 19 3 12 2 5z"/>
      </svg>
      <span>(202) 555-0187</span>
    </li>
    <li class="contact__item">
      <svg class="contact__icon" viewBox="0 0 22 22">
        <rect x="1.5" y="4" width="19" height="14"/>
        <path d="M1.5 4l9.5 8 9.5-8M1.5 18l7-6.5M20.5 18l-7-6.5"/>
      </svg>
      <span>Daniel@HollerbyWhitlock.com</span>
    </li>
  </ul>
</section>

</body>
</html>
```